Seafood Retailer requires varies packaging labels

We are an established business (Restaurant, Seafood Retailer and Crayfish Wholesaler). We have just got a new logo which covers all three aspects of our business (via Artbazaar!). We have always sold cellar door but have been asked by several food outlets to stock our product but as you will see from our pictures - it needs some serious work to take us to the next level. We have a well known finer dining restaurant which we use all these products in and is how several products came about on our Seafood shop shelves. The products are of high quality (just not the labelling). We now want to package our Seafood Retail Shop with professional packaging and labelling and reflect the "quality and freshness" of our products. We have several items we want to label as per below.

If we were to use a slogan it would be "Its about the Freshness and Quality" but not necessary.

We are after a label for our Pickled Seafood 350g tub (Various) - conical container 9cm high x 9cm (top), 7cm (bottom) ONLY but will also try and utilise it to be consistent with the other products following.

Salt and Pepper MIx 250g - conical container (as above)
Smoked Fish (Various weight & fish) - 21cm x 25cm vacuum sealed bags.
Kilpatrick Sauce 250ml - square bottle 22cm high x 4.5cm wide
Minty Lime Vinaigrette 250ml - 23cm round bottle - 4.7cm dia.
Smoked Spicy Salt 75g- 13cm wide x 16cm high vacuum bag
Dukkah 75g - 13cm wide x 16cm high vacuum bag
Lobster Oil 150ml - 18cm x 4.5cm dia round bottle

We will need a working file so we can change the names for the pickled seafood as needed.

I have attached photos of our current products for true understanding of what we currently have had to get by and where we wish to go.

We have a label printer that can print black type overs eg the name of each product so we can have generic coloured labels which we can print over with the change of each product.

We want something that will become a recognisable label.
Updates

Attn Designers.
We are only after one design but which we will use as a guide for all the options supplied as a starting point. The Pickled containers will probably be where we start but happy with any submissions. I probably wasnt very clear but wanted to show all the things we will be using the labelling for so that we can get some continuity We are just after some direction on a good look.  Thanks Marlo

Reason: Had some technical problems and wish to extend the time to allow more time conversing with designers.

Target Market(s)

Our target market varies but generally 30 - 65 years in the more affluent background. We are located "literally in the middle of a paddock in the middle of nowhere" (near several holiday villages) and it is the reputation of our premium, fresh products that have people returning and amazed on their first experience.

Industry/Entity Type

Restaurant

Requirements
Must have
• All:

Our logo and the colours are:
Orange
C 13%
M 79%
Y 100%
K 3%

Blue
C 100%
M 96%
Y 14%
K 3%

weight

nutrition panel, barcode (but we can also do that as a separate label on the back ourselves if needed)

"Produced & packaged by:
Harbourline Catch Pty Ltd, 40731 Pellam Highway, Tondarra SA 5592
Ph: 08 86120394"

Made in Australia from local and imported ingredients. Keep refrigerated. Store at 1oC - 4oC. Use in 7 days after opening.

Nice to have
• Pickled seafood - "Gourmet Pickled" and "Ready to Eat"
Should not have
• Use only the "Harbourline Catch" logo (not the "harbourline Restaurant & Seafood Sales or Restaurant Only logos)

```html
<!DOCTYPE html>
<html lang="en">
<head>
<meta charset="utf-8">
<title>Harbourline Catch – Gourmet Pickled tub label</title>
<link rel="stylesheet" href="https://fonts.googleapis.com/css2?family=Arimo:wght@400;700&family=Cinzel:wght@700&family=Courgette&family=Delius&display=swap">
<style>
:root{
  --stage:#a8a8a8;
  --paper:#ffffff;
  --brand-blue:#1f2ab0;
  --band-blue:#2a36c4;
  --band-light:#c9ccf2;
  --ink-blue:#2630c0;
  --ink-dark:#1b1b1b;
  --ornament-light:#f1f1f1;
  --ornament-mid:#d2d2d2;
  --base-grey:#d9d9d9;
  --caption:#f2f2f2;
}
*{margin:0;padding:0;box-sizing:border-box}
html,body{width:1200px;height:1000px;overflow:hidden}
body{background:var(--stage);position:relative;font-family:"Arimo",Arial,sans-serif}

.lid-label{position:absolute;left:55px;top:130px;width:320px;height:320px;border-radius:50%;
  background:linear-gradient(135deg,var(--band-light),var(--band-blue) 55%,#e6e7f8);padding:9px;
  box-shadow:2px 3px 6px rgba(0,0,0,.25)}
.lid-face{width:100%;height:100%;border-radius:50%;background:var(--paper);position:relative}

.ornament{position:absolute;border-radius:50%;
  background:radial-gradient(ellipse at 50% 40%,var(--ornament-light),var(--ornament-mid) 70%,#bdbdbd)}
.brand-name{position:absolute;left:0;right:0;text-align:center;font-family:"Arimo",Arial,sans-serif;
  font-weight:700;color:var(--brand-blue);text-transform:uppercase;letter-spacing:.5px}
.product-name{position:absolute;left:0;right:0;text-align:center;font-family:"Cinzel",serif;
  font-weight:700;color:var(--ink-dark)}

.flat-label{position:absolute;left:477px;top:152px;width:650px;height:236px;background:var(--paper);
  box-shadow:3px 4px 6px rgba(0,0,0,.25)}
.flat-label .top-band{position:absolute;left:0;top:0;width:100%;height:13px;
  background:linear-gradient(90deg,var(--band-blue),var(--band-light) 55%,var(--band-blue))}
.flat-label .base-strip{position:absolute;left:0;bottom:0;width:100%;height:13px;background:var(--base-grey)}

.info-block{position:absolute;color:var(--ink-blue);font-size:9.5px;line-height:13px;text-align:center}
.ready-badge{display:inline-block;font-family:"Courgette",cursive;font-size:13px;border:1px dashed var(--ink-blue);
  padding:2px 8px;margin:3px 0 6px}
.maker-block{position:absolute;color:var(--ink-blue);font-size:8.5px;line-height:10.5px;text-align:center}

.caption{position:absolute;font-family:"Delius",cursive;font-size:17px;color:var(--caption);letter-spacing:.5px}
.arrow{position:absolute}

.conical-label{position:absolute;left:0;top:0}
.cone-content{position:absolute}
</style>
</head>
<body>

<!-- Lid label -->
<div class="lid-label">
  <div class="lid-face">
    <div class="ornament" style="left:40px;top:55px;width:222px;height:190px" role="img" aria-label="Decorative scalloped oval frame with pearl dots in soft greys"></div>
    <div class="brand-name" style="top:122px;font-size:21px">Harbourline Catch</div>
    <div class="product-name" style="top:182px;font-size:13px">Gourmet Pickled</div>
  </div>
</div>

<div class="caption" style="left:243px;top:458px">Cup Label (optional)</div>
<svg class="arrow" style="left:172px;top:452px" width="62" height="52" viewBox="0 0 62 52">
  <path d="M18 2h26v22h16L31 50 2 24h16z" fill="#e9e9e9" stroke="#8a8a8a" stroke-width="1"/>
</svg>

<!-- Flat pattern -->
<div class="flat-label">
  <div class="top-band"></div>
  <div class="info-block" style="left:10px;top:66px;width:170px">
    Made in Australia<br>
    <span class="ready-badge">Ready to Eat</span><br>
    from local and imported ingredients.<br>
    Keep Refrigerated at 1oC-4oC.<br>
    Use in 7 days after opening<br>
    weight: 350g
  </div>
  <div class="ornament" style="left:210px;top:28px;width:230px;height:172px" role="img" aria-label="Decorative scalloped oval frame with pearl dots in soft greys"></div>
  <div class="brand-name" style="left:210px;width:230px;top:86px;font-size:19px">Harbourline Catch</div>
  <div class="product-name" style="left:210px;width:230px;top:146px;font-size:12px">Gourmet Pickled</div>
  <div class="maker-block" style="left:470px;top:100px;width:180px">
    Produced &amp; packaged by:<br>
    Harbourline Catch Pty Ltd,<br>
    40731 Pellam Highway, Tondarra SA 5592<br>
    Ph: 08 86120394*
  </div>
  <div class="base-strip"></div>
</div>

<div class="caption" style="left:738px;top:410px">Flatten pattern</div>
<svg class="arrow" style="left:766px;top:442px" width="62" height="52" viewBox="0 0 62 52">
  <path d="M18 2h26v22h16L31 50 2 24h16z" fill="#e9e9e9" stroke="#8a8a8a" stroke-width="1"/>
</svg>
<div class="caption" style="left:733px;top:512px">Conical pattern</div>

<!-- Conical pattern -->
<svg class="conical-label" width="1200" height="1000" viewBox="0 0 1200 1000">
  <defs>
    <linearGradient id="coneBand" x1="0" x2="1">
      <stop offset="0" stop-color="#2a36c4"/>
      <stop offset=".5" stop-color="#c9ccf2"/>
      <stop offset="1" stop-color="#2a36c4"/>
    </linearGradient>
    <clipPath id="coneClip">
      <path d="M425 600 A1351.6 1351.6 0 0 1 1165 600 L1105 815 A1141.5 1141.5 0 0 0 490 815 Z"/>
    </clipPath>
  </defs>
  <path d="M428 604 A1351.6 1351.6 0 0 1 1168 604 L1108 819 A1141.5 1141.5 0 0 0 493 819 Z" fill="rgba(0,0,0,.2)"/>
  <g clip-path="url(#coneClip)">
    <rect x="400" y="520" width="800" height="320" fill="#ffffff"/>
    <path d="M425 600 A1351.6 1351.6 0 0 1 1165 600" fill="none" stroke="url(#coneBand)" stroke-width="22"/>
    <path d="M490 815 A1141.5 1141.5 0 0 1 1105 815" fill="none" stroke="#d9d9d9" stroke-width="24"/>
  </g>
</svg>
<div class="info-block" style="left:470px;top:638px;width:180px;transform:rotate(4deg)">
  Made in Australia<br>
  <span class="ready-badge">Ready to Eat</span><br>
  from local and imported ingredients.<br>
  Keep Refrigerated at 1oC-4oC.<br>
  Use in 7 days after opening<br>
  weight: 350g
</div>
<div class="ornament" style="left:670px;top:588px;width:230px;height:170px" role="img" aria-label="Decorative scalloped oval frame with pearl dots in soft greys"></div>
<div class="brand-name" style="left:670px;width:230px;top:645px;font-size:19px">Harbourline Catch</div>
<div class="product-name" style="left:670px;width:230px;top:702px;font-size:12px">Gourmet Pickled</div>
<div class="maker-block" style="left:940px;top:668px;width:190px;transform:rotate(-4deg)">
  Produced &amp; packaged by:<br>
  Harbourline Catch Pty Ltd,<br>
  40731 Pellam Highway, Tondarra SA 5592<br>
  Ph: 08 86120394*
</div>

</body>
</html>
```